K & D A/C Compressors' Business Card

Hello,

I need someone to create a new business card for my business. The name of my Business is: K & D A/C Compressors. I sell automotive air conditioning parts (a/c parts). I would like the business card to incorporate my logo, and to have an automotive feel to it. It is important that the business card feel like it is coming from an automotive parts business.

I already have a logo, which I will provide.

Thanks.
Updates

Project Deadline Extended Reason: I feel like extending the deadline until October 9, 2017, will allow for more time to design the business card. Thank you for your understanding. Added Monday, October 2, 2017

Target Market(s)

Consumers who need automotive a/c parts, and auto mechanics.

Industry/Entity Type

Automotive

Contact Information for Business Card

Business name: K & D A/C Compressors
Business Address: 48207 Southwest 36th Street, North Miami Beach, Florida 33162
Telephone: 305-472-1390
Fax: To be provided once I choose your design.
Website: www.kdcoolunits.example
Email: support@kdcoolunits.example
Names: To be provided once I choose your design.

Font styles to use
Sans Serif

Colors

Designer to choose colors to be used in the design.

Requirements
Must have
• The business card must include all of the "Business Card Details" and the logo I have uploaded.

```html
<!DOCTYPE html>
<html lang="en">
<head>
<meta charset="utf-8">
<title>K &amp; D A/C Compressors – Business Card</title>
<link href="https://fonts.googleapis.com/css2?family=Questrial&family=Didact+Gothic&display=swap" rel="stylesheet">
<style>
  :root {
    --backdrop: #6e6e6e;
    --paper: #f4f4f4;
    --paper-shade: #e6e6e6;
    --sky: #94cfeb;
    --electric: #0b9ad8;
    --charcoal: #2e2e2f;
    --ink: #1c1c1c;
    --logo-grey: #9a9a9a;
  }
  * { box-sizing: border-box; margin: 0; padding: 0; }
  html, body {
    width: 1200px; height: 876px; overflow: hidden;
    background: var(--backdrop);
  }
  .canvas {
    width: 1200px; height: 876px;
    display: flex; flex-direction: column; align-items: center; justify-content: center;
    gap: 48px;
  }
  .card {
    position: relative;
    width: 600px; height: 343px;
    overflow: hidden;
    box-shadow: 0 10px 24px rgba(0,0,0,.35);
    font-family: "Didact Gothic", "Questrial", sans-serif;
  }
  .card-shapes { position: absolute; inset: 0; }

  /* front */
  .card-front { background: linear-gradient(160deg, var(--paper-shade), var(--paper) 60%, #fafafa); }
  .wordmark {
    position: absolute;
    display: flex; align-items: center; gap: 10px;
    font-family: "Questrial", sans-serif;
    color: var(--logo-grey);
    white-space: nowrap;
  }
  .wordmark-square { width: 14px; height: 14px; background: var(--electric); }
  .card-front .wordmark { left: 40px; top: 28px; font-size: 24px; }
  .person { position: absolute; left: 150px; top: 76px; }
  .person-name { font-family: "Questrial", sans-serif; font-weight: 700; font-size: 30px; color: var(--ink); letter-spacing: .2px; }
  .person-title { font-size: 14px; color: #333; margin-top: 2px; }
  .title-rule { width: 52px; height: 4px; background: var(--electric); margin-top: 6px; }
  .contact-list { position: absolute; left: 150px; top: 152px; list-style: none; font-size: 15px; color: #2a2a2a; line-height: 22px; }
  .contact-web { font-weight: 700; color: var(--ink); font-family: "Questrial", sans-serif; }
  .address {
    position: absolute; right: 40px; bottom: 22px;
    text-align: right; font-size: 16px; line-height: 23px; color: var(--ink);
    font-style: normal;
  }

  /* back */
  .card-back { background: linear-gradient(135deg, #3a3a3b, var(--charcoal) 55%, #252526); }
  .back-brand {
    position: absolute; left: 0; right: 0; top: 140px;
    display: flex; flex-direction: column; align-items: center; gap: 10px;
  }
  .card-back .wordmark { position: static; font-size: 30px; color: #a8a8a8; }
  .back-web { font-family: "Questrial", sans-serif; font-size: 20px; color: var(--electric); letter-spacing: .3px; }
</style>
</head>
<body>
<main class="canvas">

  <section class="card card-front" aria-label="Business card front">
    <svg class="card-shapes" viewBox="0 0 600 343" aria-hidden="true">
      <polygon points="0,110 70,110 165,343 0,343" fill="var(--sky)"/>
      <polygon points="430,0 600,0 600,343 545,343 470,175 520,205 445,70" fill="var(--sky)"/>
    </svg>

    <div class="wordmark"><span class="wordmark-square"></span>K &amp; D A/C Compressors</div>

    <div class="person">
      <h1 class="person-name">Marcus Bell</h1>
      <p class="person-title">President &amp; CEO</p>
      <div class="title-rule"></div>
    </div>

    <ul class="contact-list">
      <li>305-472-1390</li>
      <li>305-472-1391</li>
      <li>support@kdcoolunits.example</li>
      <li class="contact-web">www.kdcoolunits.example</li>
    </ul>

    <address class="address">
      48207 Southwest 36th Street<br>
      Bayview Springs<br>
      Texas 75510
    </address>
  </section>

  <section class="card card-back" aria-label="Business card back">
    <svg class="card-shapes" viewBox="0 0 600 343" aria-hidden="true">
      <polygon points="0,0 60,0 0,150" fill="var(--electric)"/>
      <polygon points="0,0 110,0 60,95 145,70 0,250" fill="var(--electric)"/>
      <polygon points="500,0 600,0 600,343 555,343 600,190 470,240 540,120" fill="var(--electric)"/>
    </svg>
    <div class="back-brand">
      <div class="wordmark"><span class="wordmark-square"></span>K &amp; D A/C Compressors</div>
      <p class="back-web">www.kdcoolunits.example</p>
    </div>
  </section>

</main>
</body>
</html>
```